Designing a brochures for an educational counseling service provider

We would like a 4 sided design on a 11x8.5 paper, half folded. I have including a sample design we did to give you an idea of what we envision but we welcome creativity to make beautiful looking flyers. Text for the flier is included as well as our logo.
- The most important thing is capturing our audience/market. We will be handing these flies to schools, organizations and individual clients.

www.plorvaeducationalconsultants.example

Target Market(s)

We are targeting international students wanting to study in the U.S and Canada.

Industry/Entity Type

Education

Requirements
Must have
• - Clean and clear
• - Our logo should visible and well placed.
• - Could you the pictures of students, libraries and school buildings or you could use the pictures we already have.
Nice to have
• We would like this to match business cards.

```html
<!DOCTYPE html>
<html lang="en">
<head>
<meta charset="utf-8">
<title>Plorva International Educational Consultants – Brochure Cover Spread</title>
<link rel="stylesheet" href="https://fonts.googleapis.com/css2?family=Open+Sans:wght@400;600;700;800&family=Roboto+Condensed:wght@300;400&display=swap">
<style>
  :root {
    --backdrop: #4b4b4b;
    --paper: #ffffff;
    --paper-tint: #eef0f3;
    --navy: #0a1a33;
    --navy-deep: #06132a;
    --blue: #0d4f9c;
    --blue-bright: #1673c8;
    --blue-light: #2b86d6;
    --orange: #ef7a22;
    --orange-deep: #d2561a;
    --ink: #0c2a5a;
    --white: #ffffff;
  }
  * { box-sizing: border-box; margin: 0; padding: 0; }
  html, body { width: 1200px; height: 1200px; overflow: hidden; }
  body {
    background: var(--backdrop);
    font-family: "Open Sans", Arial, sans-serif;
    display: flex; align-items: center; justify-content: center;
  }
  .spread {
    width: 1100px; height: 850px;
    display: flex;
    box-shadow: 0 20px 50px rgba(0,0,0,.45);
  }
  .panel {
    position: relative; width: 550px; height: 850px;
    background: linear-gradient(180deg, var(--paper) 0%, var(--paper-tint) 100%);
    overflow: hidden;
  }
  .panel--back { border-right: 1px solid #d5d9df; }

  /* header area */
  .panel-header { height: 190px; position: relative; }
  .role-title { position: absolute; left: 150px; top: 90px; line-height: 1.1; }
  .role-title__line1 { color: var(--blue-light); font-size: 18px; font-weight: 400; letter-spacing: 1px; text-transform: uppercase; }
  .role-title__line2 { color: var(--ink); font-size: 24px; font-weight: 800; letter-spacing: 2px; text-transform: uppercase; }

  .brand { position: absolute; left: 120px; top: 60px; display: flex; align-items: center; gap: 14px; }
  .brand__mark { width: 54px; height: 54px; border-radius: 50%; background: var(--blue); flex: none; }
  .brand__name { color: var(--ink); font-weight: 700; font-size: 18px; line-height: 1.15; text-transform: uppercase; letter-spacing: 1px; }

  /* stripes */
  .stripes { height: 14px; }
  .stripes span { display: block; }
  .stripes .s-orange { height: 8px; background: var(--orange); }
  .stripes .s-blue { height: 6px; background: var(--blue); }

  .photo { height: 300px; }
  .photo--team { background: linear-gradient(135deg, #c9b67a 0%, #e9e4d6 40%, #8a6a4c 75%, #f2f2f0 100%); }
  .photo--library { background: linear-gradient(135deg, #3a2c24 0%, #7a4a38 35%, #b84a4a 60%, #e9c79a 100%); }

  .band-dark {
    height: 66px; background: linear-gradient(90deg, var(--navy-deep), var(--navy));
    color: var(--white); display: flex; align-items: center; justify-content: center;
  }
  .band-dark h2 { font-size: 22px; font-weight: 400; letter-spacing: 2px; }
  .tagline { font-size: 15px; text-align: center; line-height: 1.35; padding: 0 30px; }

  .band-blue {
    background: linear-gradient(180deg, var(--blue) 0%, var(--blue-bright) 100%);
    color: var(--white);
  }
  .contact-block { height: 160px; padding: 28px 0 0; text-align: center; }
  .contact-block__company { font-size: 19px; letter-spacing: 1px; }
  .contact-block__address { font-size: 13px; margin-top: 8px; display: flex; justify-content: center; align-items: center; gap: 6px; }
  .contact-block__phone { font-size: 30px; font-weight: 700; margin-top: 8px; display: flex; justify-content: center; align-items: center; gap: 10px; letter-spacing: 1px; }

  .band-orange {
    height: 70px; background: linear-gradient(90deg, var(--orange-deep), var(--orange));
    color: var(--white); display: flex; align-items: center; justify-content: center; gap: 10px;
    font-size: 17px;
  }
  .panel-foot { position: relative; height: 50px; }
  .panel-foot .slashes { position: absolute; left: 24px; top: 14px; }
  .panel--front .panel-foot .slashes { left: auto; right: 24px; }

  /* services */
  .services { height: 160px; display: flex; justify-content: space-around; align-items: flex-start; padding: 26px 16px 0; }
  .service { width: 120px; display: flex; flex-direction: column; align-items: center; gap: 10px; }
  .service__icon {
    width: 64px; height: 64px; border-radius: 50%; background: var(--white);
    border: 3px solid #e6b88f; display: flex; align-items: center; justify-content: center;
  }
  .service__label { font-family: "Roboto Condensed", "Arial Narrow", sans-serif; font-weight: 300; font-size: 13px; text-transform: uppercase; text-align: center; }
  .info-pill {
    margin: 0 20px 0 auto; width: 330px; height: 26px; border-radius: 13px;
    background: var(--navy); color: var(--white); font-size: 10px;
    display: flex; align-items: center; justify-content: center; gap: 6px;
    position: relative; top: -6px;
  }
  .band-orange--front { justify-content: flex-start; padding-left: 30px; font-size: 30px; font-weight: 700; font-family: "Roboto Condensed", "Arial Narrow", sans-serif; }
  .services-wrap { height: 200px; }
</style>
</head>
<body>
  <main class="spread">
    <!-- back cover -->
    <section class="panel panel--back">
      <header class="panel-header">
        <div class="role-title">
          <p class="role-title__line1">Executive Director &amp; Independent</p>
          <p class="role-title__line2">Educational Consultant</p>
        </div>
      </header>
      <div class="stripes"><span class="s-orange"></span><span class="s-blue"></span></div>
      <div class="photo photo--team" role="img" aria-label="Photo of smiling students in sports jerseys holding a soccer ball on a field"></div>
      <div class="band-dark"><h2>CONTACT US</h2></div>
      <div class="band-blue contact-block">
        <p class="contact-block__company">Plorva International Educational Consultants, LLC</p>
        <p class="contact-block__address">
          <svg width="11" height="14" viewBox="0 0 11 14" aria-hidden="true"><path d="M5.5 0C2.5 0 0 2.4 0 5.4 0 9.2 5.5 14 5.5 14S11 9.2 11 5.4C11 2.4 8.5 0 5.5 0zm0 7.6a2.2 2.2 0 110-4.4 2.2 2.2 0 010 4.4z" fill="#fff"/></svg>
          1180 Linden Road Suite 310, Maple Hollow, TX 75010
        </p>
        <p class="contact-block__phone">
          <svg width="24" height="24" viewBox="0 0 24 24" aria-hidden="true"><path d="M6.6 10.8a15.1 15.1 0 006.6 6.6l2.2-2.2a1 1 0 011-.25 11.4 11.4 0 003.6.57 1 1 0 011 1V20a1 1 0 01-1 1A17 17 0 013 4a1 1 0 011-1h3.5a1 1 0 011 1c0 1.25.2 2.45.57 3.57a1 1 0 01-.25 1z" fill="#fff"/></svg>
          555-210-4477
        </p>
      </div>
      <div class="band-orange">
        <svg width="18" height="13" viewBox="0 0 18 13" aria-hidden="true"><rect x="0.5" y="0.5" width="17" height="12" fill="#fff"/><path d="M1 1l8 6 8-6" stroke="#ef7a22" stroke-width="1.4" fill="none"/></svg>
        claire@plorvaeducationalconsultants.example
      </div>
      <footer class="panel-foot">
        <svg class="slashes" width="40" height="22" viewBox="0 0 40 22" aria-hidden="true"><path d="M2 22L12 0M12 22L22 0" stroke="#ef7a22" stroke-width="3"/></svg>
      </footer>
    </section>

    <!-- front cover -->
    <section class="panel panel--front">
      <header class="panel-header">
        <div class="brand">
          <span class="brand__mark" aria-hidden="true"></span>
          <span class="brand__name">Plorva International<br>Educational Consultants</span>
        </div>
      </header>
      <div class="stripes"><span class="s-orange"></span><span class="s-blue"></span></div>
      <div class="photo photo--library" role="img" aria-label="Photo of three students reading together in a library in front of bookshelves"></div>
      <div class="band-dark">
        <p class="tagline">A full-service international educational consulting group serving students and families across the globe.</p>
      </div>
      <div class="band-blue services-wrap">
        <ul class="services" style="list-style:none">
          <li class="service">
            <span class="service__icon"><svg width="32" height="32" viewBox="0 0 32 32" aria-hidden="true" fill="none" stroke="#7a7f88" stroke-width="1.6"><path d="M4 12L16 5l12 7z"/><path d="M7 13v11M12 13v11M16 13v11M20 13v11M25 13v11M4 26h24"/></svg></span>
            <span class="service__label">Boarding Schools</span>
          </li>
          <li class="service">
            <span class="service__icon"><svg width="32" height="32" viewBox="0 0 32 32" aria-hidden="true" fill="none" stroke="#7a7f88" stroke-width="1.6"><path d="M9 5h11l5 5v17H9z"/><path d="M20 5v5h5M13 15h8M13 19h8M13 23h5"/></svg></span>
            <span class="service__label">College Admission</span>
          </li>
          <li class="service">
            <span class="service__icon"><svg width="32" height="32" viewBox="0 0 32 32" aria-hidden="true" fill="none" stroke="#7a7f88" stroke-width="1.6"><circle cx="11" cy="11" r="4"/><circle cx="22" cy="13" r="3.5"/><path d="M4 25c0-5 3-8 7-8s7 3 7 8zM17 25c0-4 2-7 5-7s5 3 5 7z"/></svg></span>
            <span class="service__label">Transfer Students</span>
          </li>
          <li class="service">
            <span class="service__icon"><svg width="32" height="32" viewBox="0 0 32 32" aria-hidden="true" fill="none" stroke="#7a7f88" stroke-width="1.6"><path d="M2 12l14-6 14 6-14 6z"/><path d="M8 15v7c4 3 12 3 16 0v-7M28 13v7"/></svg></span>
            <span class="service__label">Graduate Students</span>
          </li>
        </ul>
        <p class="info-pill"><span>Maple Hollow,Texas</span><span>|</span><span>info@plorvaeducationalconsultants.example</span></p>
      </div>
      <div class="band-orange band-orange--front">+1-555-210-4477</div>
      <footer class="panel-foot">
        <svg class="slashes" width="40" height="22" viewBox="0 0 40 22" aria-hidden="true"><path d="M18 22L28 0M28 22L38 0" stroke="#ef7a22" stroke-width="3"/></svg>
      </footer>
    </section>
  </main>
</body>
</html>
```